Gutschein für Fotograf
Designer PelaWix hat meinen Geschmack am besten getroffen, ging auf meine Änderungsvorschläge genau ein, und änderte Details zu meiner vollsten Zufriedenheit. Kann ich auf alle Fälle weiter empfehlen.
Zielgruppe
Ich bin Fotograf und suche nach einem Gutschein für meine Arbeiten. Zielgruppen sind Privatpersonen, Pärchenfotos, Hochzeit, Baby usw.
Aufgabenstellung
Der Gutschein sollte zu meiner Homepage passen und auch zu meinen Bildern/ meinem Stil.
Folgendes könnte darauf stehen: (Foto) Gutschein - einzulösen bei - meine Homepage sollte darauf sein - es sollte eine Version mit 50 € sein und eine mit 100€ geben. Mir gefällt wahrscheinlich etwas klassisches besser, aber auch retro/ vintage könnte ich mir gut vorstellen. Vor allem möchte ich aber, dass es weiblich/ feminin wirkt. Ob Bilder von mir auf dem Gutschein von Vorteil sind, kann ich leider nicht einschätzen, aber die Bilder können jederzeit von meiner Homepage zu Testzwecken verwendet werden.

```html
<!DOCTYPE html>
<html lang="de">
<head>
<meta charset="utf-8">
<title>Gutschein – Lukas Brandner Fotografie</title>
<link rel="stylesheet" href="https://fonts.googleapis.com/css2?family=Jura:wght@400;500;600;700&family=Alex+Brush&display=swap">
<style>
  :root {
    --page: #ffffff;
    --card: #8e8e8e;
    --card-dark: #858585;
    --fold: rgba(0,0,0,0.10);
    --panel: #ffffff;
    --ink: #1a1a1a;
    --body-text: #e4e4e4;
    --field-start: #cfcfcf;
  }
  * { margin: 0; padding: 0; box-sizing: border-box; }
  html, body { width: 1200px; height: 630px; overflow: hidden; background: var(--page); }
  body { position: relative; font-family: "Jura", sans-serif; color: var(--ink); }

  .card {
    position: absolute; left: 56px; width: 1092px; height: 258px;
    background: linear-gradient(90deg, var(--card) 0%, var(--card-dark) 50%, var(--card) 100%);
    box-shadow: 2px 3px 6px rgba(0,0,0,0.45);
  }
  .card--outside { top: 44px; }
  .card--inside { top: 331px; }
  .card::after {
    content: ""; position: absolute; left: 553px; top: 0; width: 2px; height: 100%;
    background: var(--fold);
  }

  .contact {
    position: absolute; left: 94px; top: 37px; width: 188px; height: 183px;
    background: var(--panel); border-radius: 10px;
    padding: 12px 10px; font-size: 10.4px; line-height: 13px;
  }
  .contact__title { font-weight: 600; margin-bottom: 14px; }
  .contact__block { margin-bottom: 12px; }
  .contact__social { display: flex; align-items: center; gap: 5px; margin-top: 8px; }
  .contact__social-mark { width: 18px; height: 18px; border-radius: 3px; background: #6b6b6b; }

  .portrait {
    position: absolute; left: 306px; top: 38px; width: 132px; height: 181px;
    border-radius: 9px;
    background: linear-gradient(160deg, #2a2a2a 0%, #5c5c5c 55%, #3a3a3a 100%);
  }

  .title-badge {
    position: absolute; left: 646px; top: 194px; width: 344px; height: 52px;
    border-radius: 9px;
    background: linear-gradient(90deg, #cfcfcf 0%, #ffffff 40%);
    display: flex; align-items: center; justify-content: center;
    font-size: 52px; font-weight: 600; letter-spacing: 2px; line-height: 1;
  }

  .photo-strip { position: absolute; left: 1px; top: 35px; height: 100px; display: flex; }
  .photo-strip__item { height: 100%; }
  .photo-strip__item--portrait { width: 71px; background: linear-gradient(135deg,#1e1e1e,#6a6a6a); }
  .photo-strip__item--wedding { width: 128px; background: linear-gradient(135deg,#3a3a3a,#d8d8d8); }
  .photo-strip__item--group { width: 134px; background: linear-gradient(180deg,#e6e6e6,#2e2e2e); }
  .photo-strip__item--child { width: 76px; background: linear-gradient(135deg,#bdbdbd,#4a4a4a); }
  .photo-strip__item--interior { width: 152px; background: linear-gradient(135deg,#d0d0d0,#f4f4f4); }

  .about {
    position: absolute; left: 20px; top: 151px; width: 542px;
    font-size: 10.3px; line-height: 13.1px; color: var(--body-text);
    text-align: justify; text-align-last: justify;
  }

  .field {
    position: absolute; left: 646px; width: 373px;
    border-radius: 9px;
    background: linear-gradient(90deg, var(--field-start) 0%, #ffffff 45%);
    font-size: 10.4px;
  }
  .field--recipient { top: 60px; height: 32px; }
  .field--value { top: 110px; height: 32px; }
  .field--sign { top: 159px; height: 52px; }
  .field__label { position: absolute; left: 8px; top: 11px; }
  .field__amount {
    position: absolute; left: 50px; top: -2px;
    font-family: "Alex Brush", cursive; font-size: 30px; color: var(--ink);
  }
  .field__foot { position: absolute; bottom: 2px; font-size: 10.4px; }
  .field__foot--date { left: 7px; }
  .field__foot--stamp { right: 31px; }
</style>
</head>
<body>
  <section class="card card--outside">
    <div class="contact">
      <p class="contact__title">Kontakt:</p>
      <p class="contact__block">Fotograf<br>Lukas Brandner<br>Lindenhofgasse 7<br>A - 3820 Raabs</p>
      <p>Handy: 06601234567<br>Email: info@lukasbrandner-foto.at<br>http://www.lukasbrandner-foto.at</p>
      <p class="contact__social"><span class="contact__social-mark"></span>/lukasbrandnerfotografie</p>
    </div>
    <div class="portrait" role="img" aria-label="Schwarzweiß-Porträt des Fotografen mit Kamera"></div>
    <div class="title-badge">GUTSCHEIN</div>
  </section>

  <section class="card card--inside">
    <div class="photo-strip">
      <div class="photo-strip__item photo-strip__item--portrait" role="img" aria-label="Schwarzweiß-Porträt einer Frau"></div>
      <div class="photo-strip__item photo-strip__item--wedding" role="img" aria-label="Hochzeitspaar in Schwarzweiß"></div>
      <div class="photo-strip__item photo-strip__item--group" role="img" aria-label="Gruppe junger Frauen in Dirndl"></div>
      <div class="photo-strip__item photo-strip__item--child" role="img" aria-label="Lachendes Kind"></div>
      <div class="photo-strip__item photo-strip__item--interior" role="img" aria-label="Helles modernes Badezimmer"></div>
    </div>
    <p class="about">Fotografie und andere künstlerische Aktivitäten begleiten mich schon mein ganzes Leben lang. Doch in der Fotografie habe ich meine größte Berufung gefunden, diese ist für mich bei weiten kein Hobby oder Beruf mehr, für mich bedeutet es Leben, nichts macht mir mehr Freude als wenn ich zufriedene Menschen sehe die ihre Fotos das erste Mal in den Händen halten und bestaunen. Wenn ich nicht gerade im Kundenauftrag fotografiere, dann nutze ich die Zeit um mich anderweitig fotomäßig weiterzubilden, sei es in Vorträgen, Diskussionen, Kursen oder ich starte einfach los und besuche verlassene Orte und mach dort unter oft schwierigsten Licht und Umgebungsverhältnissen Fotos.</p>

    <div class="field field--recipient"><span class="field__label">Für:</span></div>
    <div class="field field--value"><span class="field__label">Wert:</span><span class="field__amount">100 Euro</span></div>
    <div class="field field--sign">
      <span class="field__foot field__foot--date">Datum</span>
      <span class="field__foot field__foot--stamp">Stempel &amp; Unterschrift</span>
    </div>
  </section>
</body>
</html>
```